Dynamic Templates

Our company hosts web stores for our clients. They can set up as many as they wish on our platform, and select from the stock templates we provide. We are looking to increase the number of available stock templates.

Because our users can dynamically control many of the template elements - specifically colors - they have to be flexible and abide by certain rules. These rules are spelled out in the attached documents.

Here are links to two of our most used templates:
http://fernridge.vexalcart.example/
http://stampled.vexalcart.example/

Templates need to have a landing page (what you see when first clicking one of the above links). There also needs to be a category page (what you see when clicking any category) and a product detail page (what you see when you arrive at an individual product, where there are various cart options like Buy Now or Request Info).

```html
<!DOCTYPE html>
<html lang="en">
<head>
<meta charset="utf-8">
<title>LumaMerch – Distributor Website Solutions</title>
<link rel="stylesheet" href="https://fonts.googleapis.com/css2?family=Arimo:wght@400;700&family=PT+Sans:wght@400;700&display=swap">
<style>
  :root {
    --orange: #f7931e;
    --orange-dark: #f27a00;
    --orange-light: #ffc266;
    --ink: #222222;
    --text: #333333;
    --muted: #7d7d6b;
    --band: #e8e8e8;
    --white: #ffffff;
    --navy: #0f1f3a;
    --footer: #2d2d2d;
    --rule: #555555;
    --bag-red: #d41c1f;
  }
  * { box-sizing: border-box; margin: 0; padding: 0; }
  html, body { width: 1093px; height: 1200px; overflow: hidden; }
  body {
    position: relative;
    background: var(--white);
    font-family: "Arimo", Arial, sans-serif;
    color: var(--text);
  }
  .abs { position: absolute; }

  /* Header */
  .brand { left: 68px; top: 24px; display: flex; align-items: center; gap: 11px; }
  .brand-dot { width: 46px; height: 46px; border-radius: 50%; background: var(--orange); }
  .brand-name { font-size: 22px; font-weight: 700; color: var(--navy); line-height: 1; }
  .brand-tag { font-size: 11px; font-weight: 700; color: var(--muted); letter-spacing: .4px; margin-top: 6px; }
  .top-contact { right: 64px; top: 35px; font-size: 12.5px; font-weight: 700; color: #000; }
  .top-contact a { color: var(--orange-dark); text-decoration: none; }

  /* Navigation */
  .nav {
    left: 57px; top: 92px; width: 977px; height: 50px; border-radius: 25px;
    background: linear-gradient(#ffcf7a 0%, #fbb041 45%, #f7961f 100%);
    box-shadow: 0 10px 14px -8px rgba(247,147,30,.35);
  }
  .nav-item {
    position: absolute; top: 0; height: 50px; line-height: 50px;
    font-family: "PT Sans", "Trebuchet MS", sans-serif; font-size: 19px;
    color: var(--ink); transform: translateX(-50%); white-space: nowrap;
  }
  .nav-item.is-active { color: var(--white); }
  .nav-divider { position: absolute; top: 4px; width: 1px; height: 42px; background: rgba(200,100,0,.45); box-shadow: 1px 0 0 rgba(255,230,180,.6); }

  /* Hero band */
  .band { left: 0; top: 288px; width: 1093px; height: 419px; background: var(--band); }
  .showcase {
    left: 54px; top: 183px; width: 983px; height: 210px;
    border: 3px solid var(--orange); border-radius: 30px; background: var(--white);
  }
  .product { position: absolute; border-radius: 6px; }

  .intro { left: 89px; width: 740px; }
  .intro h2 { font-size: 19.5px; font-weight: 400; color: var(--orange-dark); line-height: 1; }
  .intro hr { border: 0; border-top: 1px dashed var(--rule); margin-top: 10px; }
  .intro p { font-size: 11.7px; line-height: 19.6px; color: var(--text); margin-top: 7px; letter-spacing: -0.1px; }
  .intro p + p { margin-top: 19.6px; }

  .promo-visual {
    left: 866px; top: 420px; width: 172px; height: 224px; border-radius: 6px;
    background: linear-gradient(135deg, #e2393b 0%, var(--bag-red) 60%, #b5161a 100%);
  }
  .start-shopping { left: 864px; top: 655px; width: 176px; text-align: center; font-size: 20px; color: #333; }

  /* Shop lists */
  .section-title { font-size: 20px; color: #333; top: 726px; }
  .dash-rule { border-top: 1px dashed var(--rule); height: 0; }
  .dash-col { border-left: 1px dashed var(--rule); width: 0; top: 789px; height: 274px; }
  .list { list-style: none; top: 778px; }
  .list li { font-size: 12px; font-weight: 700; color: var(--ink); height: 26.2px; line-height: 26.2px; white-space: nowrap; }

  /* Search + contact */
  .quick-search { left: 864px; top: 726px; width: 172px; text-align: center; font-size: 20px; color: #333; }
  .search-box {
    left: 864px; top: 760px; width: 173px; height: 33px;
    border: 3px solid var(--orange); border-radius: 17px; background: var(--white);
  }
  .search-go {
    position: absolute; right: 2px; top: 2px; width: 42px; height: 23px; border-radius: 12px;
    background: var(--navy); color: var(--white); font-size: 17px; text-align: center; line-height: 23px;
  }
  .contact-box {
    left: 864px; top: 820px; width: 173px; height: 106px;
    border: 3px solid var(--orange); border-radius: 26px; background: var(--white);
  }
  .contact-box h3 { font-size: 20px; font-weight: 400; color: #333; margin: 12px 0 0 25px; }
  .contact-box a { display: block; font-size: 11.5px; font-weight: 700; color: var(--orange-dark); text-decoration: none; text-align: center; line-height: 18px; white-space: nowrap; }
  .contact-box h3 + a { margin-top: 6px; }

  /* Footer */
  .footer { left: 0; top: 1107px; width: 1093px; height: 93px; background: var(--footer); color: var(--white); font-size: 12px; text-align: center; line-height: 98px; }
</style>
</head>
<body>

<header>
  <div class="brand abs">
    <span class="brand-dot"></span>
    <div>
      <div class="brand-name">LumaMerch</div>
      <div class="brand-tag">DISTRIBUTOR WEBSITE SOLUTIONS</div>
    </div>
  </div>
  <div class="top-contact abs">Demo User . (415) 555-0142 . <a href="#">info@lumamerch.example</a></div>

  <nav class="nav abs">
    <span class="nav-item is-active" style="left:86px">Home</span>
    <span class="nav-divider" style="left:170px"></span>
    <span class="nav-item" style="left:266px">About Us</span>
    <span class="nav-divider" style="left:361px"></span>
    <span class="nav-item" style="left:463px">Our Works</span>
    <span class="nav-divider" style="left:563px"></span>
    <span class="nav-item" style="left:666px">Categories</span>
    <span class="nav-divider" style="left:769px"></span>
    <span class="nav-item" style="left:871px">Contact Us</span>
  </nav>
</header>

<div class="band abs"></div>

<section class="showcase abs">
  <div class="product" role="img" aria-label="Desk puzzle toy with colourful word pieces on a black base" style="left:29px;top:10px;width:177px;height:188px;background:linear-gradient(160deg,#7fb7e0 0%,#e8c53a 35%,#5bb04c 55%,#2a2a2a 75%,#1b1b1b 100%);"></div>
  <div class="product" role="img" aria-label="Blue and white desktop calculator" style="left:302px;top:10px;width:158px;height:188px;border-radius:24px;background:linear-gradient(180deg,#e9ecef 0%,#c9cfd6 40%,#2f57b5 100%);"></div>
  <div class="product" role="img" aria-label="Squeaky toy hammer with yellow head and blue handle" style="left:548px;top:10px;width:142px;height:188px;background:linear-gradient(180deg,#f2e14a 0%,#f0a3b6 25%,#8cc7ef 55%,#5a9be0 100%);"></div>
  <div class="product" role="img" aria-label="Black leather portfolio with red pen and USB drive" style="left:765px;top:10px;width:185px;height:188px;background:linear-gradient(160deg,#3a3a3a 0%,#111 70%,#2b2b2b 100%);"></div>
</section>

<main>
  <section class="intro abs" style="top:423px">
    <h2>Welcome To The Future of Promotional Products!</h2>
    <hr>
    <p>Gone are the days of searching through dog-eared catalogs or trying to make sense of complicated product websites.</p>
    <p>We do the work for you! We've taken only the very best and most current products and placed them in easy-to-use categories designed for your needs. Take a look at our selection - quality products at excellent prices.</p>
  </section>

  <section class="intro abs" style="top:574px">
    <h2>Enjoy This Amazing New Resource</h2>
    <hr>
    <p>We know you don't have time to waste; so we've cut to the chase and made it simple! But keep in mind, we do have access to over a million products - so if you don't see what you're looking for or have a special theme or request, let us know - we'll find it!</p>
  </section>

  <div class="promo-visual abs" role="img" aria-label="Red holiday shopping bag with white snowflakes"></div>
  <div class="start-shopping abs">Start Shopping</div>

  <section>
    <h2 class="section-title abs" style="left:90px;font-weight:400">Shop By Category</h2>
    <div class="dash-rule abs" style="left:87px;top:762px;width:575px"></div>
    <ul class="list abs" style="left:87px">
      <li>Apparel</li><li>Bags &amp; Totes</li><li>Caps &amp; Hats</li><li>Computer</li><li>Eco Friendly</li><li>Food, Candy &amp; Drink</li><li>Golf, Sports &amp;</li><li>Outdoors</li><li>Home &amp; Housewares</li><li>Notebooks &amp; Folios</li><li>Tools &amp; Hardware</li>
    </ul>
    <div class="dash-col abs" style="left:243px"></div>
    <ul class="list abs" style="left:272px">
      <li>Auto</li><li>Business Supplies</li><li>Clocks &amp; Watches</li><li>Corporate Gifts</li><li>Electronics</li><li>Games &amp; NoveltiesGift</li><li>Sets</li><li>Healthcare &amp; Safety</li><li>KeychainsMugs &amp;</li><li>Drinkware</li><li>Stress Balls &amp;</li>
    </ul>
    <div class="dash-col abs" style="left:455px"></div>
    <ul class="list abs" style="left:483px">
      <li>Awards</li><li>&nbsp;Recognition</li><li>Calendars</li><li>Company Outings</li><li>Desktop &amp; Office</li><li>Executive Gifts</li><li>Golf</li><li>Holiday</li><li>Pocket &amp; Purse</li>
    </ul>
    <div class="dash-col abs" style="left:676px"></div>
  </section>

  <section>
    <h2 class="section-title abs" style="left:687px;font-weight:400">Shop By Price</h2>
    <div class="dash-rule abs" style="left:687px;top:762px;width:134px"></div>
    <ul class="list abs" style="left:708px">
      <li>Under $5</li><li>$5 - $10</li><li>$10 - $20</li><li>$20 - $50</li><li>$50 - $100</li><li>$100 - $200</li><li>Over $200</li>
    </ul>
  </section>

  <aside>
    <h2 class="quick-search abs" style="font-weight:400">Quick Search</h2>
    <div class="search-box abs"><span class="search-go">Go</span></div>
    <div class="contact-box abs">
      <h3>Contact Us</h3>
      <a href="#">info@lumamerch.example</a>
      <a href="#">www.lumamerch.example</a>
    </div>
  </aside>
</main>

<footer class="footer abs">Copyright © 2010 . LumaMerch.example V3 . All Rights Reserved.</footer>

</body>
</html>
```